Bramble Plumbing and Drain wrap design

I would like to incorporate my logo into the design of the wrap. I would also like "Bramble Plumbing and Drain" on the wrap. Pretty open to designs. I would also like the number '555-317-4062" I included a photo of the van I intend to wrap. You have a lot of design room on the van. Maybe try designs with more colors than white. We really want to stand out from the crowd. NOT A LOT OF PINK. I uploaded some photos of wraps that I like for a better idea. I would like to have strong bold lines. I prefer the van wrap style in the included photos that has the Marlow name on the van (image 1 and 2).

Target Market(s)

Every homeowner, real estate owner, property managers

Colors
78c3e4
f37122
33b8a4
ec1f27
ffc214
fbed22
9ccb3b
0455a3
f78f20

Requirements
Must have
• Design on both the sides and back. Also must have the logo, company name and number (in company description).
Nice to have
• Standout design! something that catches the customers eye. Maybe the background of Los Angeles, California. Nice strong bold colors and lines maybe. Clean looking but not boring. PLEASE USE VERY LITTLE PINK, IF ANY IN THE DESIGN . It's OK to just have the pink in the logo and that's it.

```html
<!DOCTYPE html>
<html lang="en">
<head>
<meta charset="utf-8">
<title>Bramble Plumbing and Drain – Truck Side Wrap</title>
<link rel="stylesheet" href="https://fonts.googleapis.com/css2?family=Montserrat:wght@800&display=swap">
<style>
  :root {
    --stage: #eceff2;
    --wrap-white: #ffffff;
    --brand-blue: #0455a3;
    --deep-blue: #023a78;
    --mid-blue: #1a6cc0;
    --navy-line: #0b3473;
    --accent-pink: #e5197f;
    --skyline-grey: #a7a8aa;
    --number-blue: #0a5aa8;
  }
  html, body {
    margin: 0;
    width: 1200px;
    height: 900px;
    overflow: hidden;
    background: var(--stage);
  }
  .wrap-stage {
    width: 1200px;
    height: 900px;
    display: flex;
    align-items: center;
    justify-content: center;
  }
  .side-panel {
    width: 1080px;
    height: 780px;
    display: block;
    box-shadow: 0 10px 30px rgba(0, 0, 0, 0.15);
  }
  .phone-number {
    font-family: "Montserrat", sans-serif;
    font-weight: 800;
    font-size: 80px;
    fill: var(--number-blue);
  }
  .brand-name {
    font-family: "Montserrat", sans-serif;
    font-weight: 800;
    font-size: 40px;
    fill: var(--brand-blue);
    text-anchor: middle;
  }
</style>
</head>
<body>
<main class="wrap-stage">
  <svg class="side-panel" viewBox="0 0 1080 780" xmlns="http://www.w3.org/2000/svg">
    <defs>
      <linearGradient id="top-field-fill" x1="0" y1="0" x2="1" y2="0.5">
        <stop offset="0" stop-color="var(--deep-blue)"/>
        <stop offset="0.55" stop-color="var(--brand-blue)"/>
        <stop offset="1" stop-color="var(--mid-blue)"/>
      </linearGradient>
      <linearGradient id="skyline-fill" x1="0" y1="0" x2="0" y2="1">
        <stop offset="0" stop-color="var(--skyline-grey)" stop-opacity="0"/>
        <stop offset="0.3" stop-color="var(--skyline-grey)" stop-opacity="0.75"/>
        <stop offset="1" stop-color="var(--skyline-grey)" stop-opacity="0.9"/>
      </linearGradient>
      <clipPath id="below-pinstripe">
        <path d="M0 295 C420 310 640 570 800 650 L800 780 L0 780 Z"/>
      </clipPath>
    </defs>

    <rect class="panel-base" width="1080" height="780" fill="var(--wrap-white)"/>

    <path class="top-field" fill="url(#top-field-fill)"
      d="M0 0 H1080 V440 C1020 520 900 535 800 480 C620 380 400 215 0 205 Z"/>

    <path class="swoosh-band" fill="var(--brand-blue)"
      d="M0 235 C420 245 640 420 820 520 C920 575 1040 560 1080 470
         L1080 560 C1030 640 920 660 800 610 C620 520 420 275 0 262 Z"/>

    <path class="pink-pinstripe" fill="none" stroke="var(--accent-pink)" stroke-width="5"
      d="M0 290 C420 305 640 565 800 645 C910 695 1040 675 1080 605"/>

    <path class="navy-pinstripe" fill="none" stroke="var(--navy-line)" stroke-width="7"
      d="M760 650 C860 720 1010 708 1080 632"/>

    <g clip-path="url(#below-pinstripe)">
      <rect class="skyline" role="img" aria-label="Grey city skyline silhouette"
        x="0" y="330" width="720" height="310" fill="url(#skyline-fill)"/>
    </g>

    <text class="phone-number" x="48" y="730">555-317-4062</text>

    <g class="brand-mark">
      <circle cx="794" cy="350" r="192" fill="var(--wrap-white)"
        stroke="var(--accent-pink)" stroke-width="8"/>
      <text class="brand-name" x="794" y="310">Bramble</text>
      <text class="brand-name" x="794" y="364">Plumbing</text>
      <text class="brand-name" x="794" y="418">and Drain</text>
    </g>
  </svg>
</main>
</body>
</html>
```